Insurance Agency Flyer

Create a flyer that encompasses the basic services that our agency offers. Flyer wording, logo, and company font are attached. See our website at www.tavumerix.com for additional details.

Target Market(s)

Prospective clients

Industry/Entity Type

Insurance Agency

Other font styles liked:
• baker signet com

```html
<!DOCTYPE html>
<html lang="en">
<head>
<meta charset="utf-8">
<title>The Tavumerix Company – Insurance Flyer</title>
<link rel="stylesheet" href="https://fonts.googleapis.com/css2?family=Cinzel:wght@400;600&family=Open+Sans:wght@400;600;700&display=swap">
<style>
  :root{
    --red:#d5162b;
    --red-dark:#a80f1f;
    --ink:#4a4a4a;
    --muted:#6b6b6b;
    --rule:#d9d9d9;
    --paper:#ffffff;
    --photo-a:#c9c2b4;
    --photo-b:#8f8676;
  }
  *{box-sizing:border-box;margin:0;padding:0}
  html,body{width:707px;height:1200px;overflow:hidden;background:var(--paper)}
  body{font-family:"Open Sans",Arial,sans-serif;color:var(--ink);position:relative}
  .hero{position:absolute;left:0;top:0;width:707px;height:420px}
  .brand{position:absolute;left:488px;top:36px;width:150px;height:150px;border-radius:50%;
    background:var(--paper);display:flex;align-items:center;justify-content:center;text-align:center;
    box-shadow:0 0 0 5px var(--red)}
  .brand-name{font-family:"Open Sans",Arial,sans-serif;font-weight:700;color:var(--red);font-size:19px;line-height:1.15}
  .content{position:absolute;left:52px;right:52px;top:425px}
  .heading{font-family:"Cinzel",Georgia,serif;color:var(--red);text-align:center;font-weight:600}
  .heading--sm{font-size:17px;letter-spacing:.5px}
  .heading--lg{font-size:21px;margin-top:16px}
  .copy{font-size:9.5px;line-height:1.55;color:var(--muted);text-align:center;margin-top:7px}
  .band{background:var(--red);color:#fff;font-family:"Cinzel",Georgia,serif;font-weight:600;
    font-size:15px;text-align:center;padding:7px 0;margin:18px -52px 0}
  .coverages{display:flex;gap:40px;margin-top:14px}
  .coverage{flex:1}
  .coverage-title{font-weight:700;font-size:14px;color:var(--ink);border-bottom:2px solid var(--red);padding-bottom:4px;margin-bottom:6px}
  .coverage ul{list-style:none}
  .coverage li{font-size:10px;line-height:1.75;padding-left:14px;position:relative;color:var(--muted)}
  .coverage li::before{content:"";position:absolute;left:2px;top:6px;width:6px;height:6px;background:var(--red);border-radius:50%}
  .quote{background:var(--red);color:#fff;margin:16px -52px 0;padding:12px 70px 12px;text-align:center;position:relative}
  .quote-mark{font-family:"Cinzel",Georgia,serif;font-size:34px;line-height:1;position:absolute;top:4px;left:34px;opacity:.85}
  .quote p{font-size:10px;line-height:1.55}
  .quote cite{display:block;font-style:normal;font-weight:700;font-size:9.5px;margin-top:5px;text-align:right}
  .footer{display:flex;justify-content:center;align-items:center;gap:14px;margin-top:14px;font-size:11px;color:var(--ink)}
  .footer .sep{width:5px;height:5px;border-radius:50%;background:var(--red)}
  .footer .web,.footer .phone{color:var(--red);font-weight:700}
  .footer svg{vertical-align:-2px;margin-right:4px}
</style>
</head>
<body>
  <svg class="hero" viewBox="0 0 707 420" aria-hidden="false">
    <defs>
      <linearGradient id="photoTone" x1="0" y1="0" x2="1" y2="1">
        <stop offset="0" stop-color="var(--photo-a)"/>
        <stop offset=".55" stop-color="#b3a991"/>
        <stop offset="1" stop-color="var(--photo-b)"/>
      </linearGradient>
    </defs>
    <rect width="707" height="420" fill="url(#photoTone)" role="img" aria-label="Photo of a red toy car beside stacks of coins on a calculator"/>
    <path d="M0 300 Q353 450 707 300 L707 420 L0 420 Z" fill="var(--red)"/>
    <path d="M0 318 Q353 462 707 318 L707 420 L0 420 Z" fill="var(--paper)"/>
  </svg>

  <div class="brand"><span class="brand-name">The<br>Tavumerix<br>Company</span></div>

  <main class="content">
    <h2 class="heading heading--sm">About Our Agency</h2>
    <p class="copy">Established in 1966, The Tavumerix Company has served families and businesses across our community with honest advice and dependable coverage. We take time to understand your needs, compare options from leading carriers and stay with you long after the policy is written.</p>

    <h2 class="heading heading--lg">A Professional Agency With Exceptional Service.</h2>
    <p class="copy">Our licensed team brings decades of experience to every conversation. Whether you are insuring your first car or protecting a growing company, we explain each choice in plain terms and help you find the right balance of protection and price for your situation.</p>

    <div class="band">We Offer Complete Insurance Services</div>

    <section class="coverages">
      <div class="coverage">
        <h3 class="coverage-title">Personal Coverages</h3>
        <ul>
          <li>Automobile</li><li>Homeowners</li><li>Renters</li><li>Motorcycle / Watercraft</li>
          <li>Personal Umbrella</li><li>Flood</li><li>Life</li><li>Health</li>
        </ul>
      </div>
      <div class="coverage">
        <h3 class="coverage-title">Business Coverages</h3>
        <ul>
          <li>Commercial Auto</li><li>General Liability</li><li>Commercial Property</li><li>Workers Compensation</li>
          <li>Professional Liability</li><li>Business Owners Policy</li><li>Surety Bonds</li><li>Group Benefits</li>
        </ul>
      </div>
    </section>

    <div class="band">We Are an Independent Insurance Agency</div>
    <p class="copy">As an independent agency, we are not tied to a single insurer. We shop multiple companies on your behalf, so you get broader choices, competitive rates and a local advocate when you need to file a claim. Our clients count on us to review their coverage every year and adjust it as their lives and businesses change.</p>

    <blockquote class="quote">
      <span class="quote-mark">&ldquo;</span>
      <p>The Tavumerix Company has been proud to serve our neighbors for generations. We look forward to earning your trust and protecting everything you have worked so hard to build.</p>
      <cite>Daniel Hollis, President</cite>
    </blockquote>

    <footer class="footer">
      <span><svg width="10" height="13" viewBox="0 0 10 13"><path d="M5 0a5 5 0 0 0-5 5c0 3.5 5 8 5 8s5-4.5 5-8a5 5 0 0 0-5-5zm0 7a2 2 0 1 1 0-4 2 2 0 0 1 0 4z" fill="var(--red)"/></svg>418 Harlow Street, Ridgeview, SC 29000</span>
      <span class="sep"></span>
      <span class="web">www.tavumerix.com</span>
      <span class="sep"></span>
      <span class="phone"><svg width="12" height="12" viewBox="0 0 24 24"><path d="M6.6 10.8a15 15 0 0 0 6.6 6.6l2.2-2.2c.3-.3.7-.4 1-.2 1.1.4 2.3.6 3.6.6.6 0 1 .4 1 1V20c0 .6-.4 1-1 1A17 17 0 0 1 3 4c0-.6.4-1 1-1h3.5c.6 0 1 .4 1 1 0 1.3.2 2.5.6 3.6.1.3 0 .7-.2 1z" fill="var(--red)"/></svg>(555) 410-2738</span>
    </footer>
  </main>
</body>
</html>
```